Drug safety monitoring company requires a new corporate website

We are an outsourcing partner to large and small companies within the pharmaceutical industry. Our current website www.orbanquill.co.uk has not been updated in a long time. We want a new web site that is responsive and modern but with a clearly corporate and professional feel. We want a design based on a 12 column grid system (mobile and desktop version). We want to use a new, modern font (not the standard web fonts) - we will purchase as required. Content can be used as is from the current website. Red and white are the corporate colours, so a palate should be developed to match. We do not need as much red as is in the current website. New icons (preferably in svg format) would be great. We can also purchase new images from PhotoVane (or other) as required. We would prefer submissions in Sketch if possible.

Target Market(s)

Pharmaceutical companies

Number of Pages Required

1 page

Font styles to use
Sans Serif

Colors
ec1f27
ffffff

Requirements
Must have
• Design based on 12 column grid system.
Responsive design (i.e. require a mobile and desktop version).
How should the menu look between desktop and mobile?
A coherent colour palete.
Content to come from the existing website: www.orbanquill.co.uk
How should links be styled?
How should headings, sub-headings, paragraphs be styled?
Nice to have
• Custom developed icons (these are along the bottom of the page on the existing website: Medical Information; Pharmacovigilance; Literature Monitoring; Training).
New imagery (the images on the current website are dated).
Submission ideally as Sketch files (but we are okay with photoshop too).
A new, modern, non-standard font.
Not so much red in the design.
If we had buttons on the website, how should they be styled?
If we had a form on the website, how should the fields be styled?

```html
<!DOCTYPE html>
<html lang="en">
<head>
<meta charset="utf-8">
<title>Orban Quill – Pharmacovigilance</title>
<link href="https://fonts.googleapis.com/css2?family=DM+Sans:wght@400;500;700&family=Yellowtail&display=swap" rel="stylesheet">
<style>
:root{
  --red:#ec3a3b;
  --red-deep:#ec1f27;
  --ink:#1d2a4d;
  --text:#2b3450;
  --muted:#8a90a3;
  --line:#dfe2ea;
  --wash:#f7f8fb;
  --white:#ffffff;
  --green:#3ecf6a;
  --blue:#3f82f0;
  --yellow:#f5c531;
}
*{box-sizing:border-box;margin:0;padding:0}
html,body{width:1200px;height:2984px;overflow:hidden}
body{position:relative;background:var(--white);font-family:"DM Sans",sans-serif;color:var(--text)}
.abs{position:absolute}
.brand{font-weight:700;font-size:19px;color:var(--red);display:flex;align-items:center;gap:7px}
.brand i{display:block;width:12px;height:12px;border:2px solid var(--red);border-radius:2px}
.btn{position:absolute;display:flex;align-items:center;justify-content:center;font-size:17px;text-decoration:none}
.btn-solid{background:var(--red);color:var(--white)}
.btn-ghost{border:1px solid var(--ink);color:var(--ink);background:var(--white)}
.label{font-size:14px;color:var(--red);letter-spacing:.2px}
.h2{font-size:34px;line-height:46px;color:var(--ink);font-weight:400}
.para{font-size:18px;line-height:31px;color:var(--text)}
.photo{position:absolute}
.round{position:absolute;border-radius:50%}
.card{position:absolute;background:var(--white);border:1px solid var(--line);box-shadow:0 4px 14px rgba(30,40,80,.06)}
.svc-title{position:absolute;left:84px;top:40px;font-size:17px;color:var(--ink)}
.svc-text{position:absolute;left:29px;top:100px;width:220px;font-size:14.5px;line-height:21px;color:var(--text)}
.svc-icon{position:absolute;left:29px;top:40px;width:40px;height:40px;border-radius:50%;display:flex;align-items:center;justify-content:center}
.arrow{position:absolute;border:1.5px solid var(--ink);border-radius:50%;display:flex;align-items:center;justify-content:center;background:var(--white)}
.foot-h{font-size:13px;font-weight:700;color:var(--ink)}
.foot-l{font-size:13px;color:var(--ink);line-height:29px}
</style>
</head>
<body>

<!-- Header -->
<header class="abs" style="left:0;top:0;width:1200px;height:95px;border-bottom:1px solid var(--line)">
  <div class="brand abs" style="left:87px;top:43px"><i></i>OrbanQuill.</div>
  <a class="btn" style="left:909px;top:23px;width:127px;height:41px;border:1px solid var(--red);color:var(--red);font-size:13px">Contact us</a>
  <div class="round" style="left:1077px;top:26px;width:34px;height:34px;background:var(--red);display:flex;align-items:center;justify-content:center">
    <svg width="14" height="11" viewBox="0 0 14 11"><path d="M0 1h14M0 5.5h14M0 10h14" stroke="#fff" stroke-width="1.3"/></svg>
  </div>
</header>

<!-- Hero -->
<section>
  <div class="abs" style="left:756px;top:127px;width:444px;height:508px;background:var(--wash)"></div>
  <h1 class="abs" style="left:87px;top:220px;width:440px;font-size:32px;line-height:46px;font-weight:400;color:var(--ink)">Orban Quill ensure that your business has the best Pharmacovigilance support in the industry.</h1>
  <a class="btn btn-solid" style="left:87px;top:441px;width:177px;height:61px">Contact us</a>
  <a class="btn btn-ghost" style="left:279px;top:441px;width:177px;height:61px">Learn more</a>

  <div class="photo" role="img" aria-label="Scientists in lab coats examining a sample" style="left:677px;top:193px;width:210px;height:253px;background:linear-gradient(160deg,#cfd3da,#8e97a6 55%,#e6e9ee)"></div>
  <div class="photo" role="img" aria-label="Hands using a tablet with a health dashboard" style="left:894px;top:193px;width:212px;height:177px;background:linear-gradient(150deg,#eceef2,#c8ccd4)"></div>
  <div class="photo" role="img" aria-label="Gloved hand pipetting samples in a lab" style="left:966px;top:378px;width:140px;height:191px;background:linear-gradient(170deg,#dfe6ee,#6f8fc4 60%,#9db4d8)"></div>
  <div class="round" style="left:908px;top:388px;width:40px;height:40px;background:var(--red);display:flex;align-items:center;justify-content:center">
    <svg width="14" height="13" viewBox="0 0 14 13"><rect x="1" y="3" width="12" height="9" rx="1.5" fill="none" stroke="#fff" stroke-width="1.3"/><path d="M5 3V1h4v2M7 5.5v4M5 7.5h4" stroke="#fff" stroke-width="1.3" fill="none"/></svg>
  </div>
  <div class="card" style="left:677px;top:454px;width:281px;height:114px">
    <div class="round" role="img" aria-label="Client portrait" style="left:23px;top:36px;width:38px;height:38px;background:#3a4150"></div>
    <div class="abs" style="right:26px;top:12px;font-size:16px;color:#bfc3cd;font-weight:700">”</div>
    <div class="abs" style="left:81px;top:34px;width:185px;font-size:13.5px;line-height:19px;color:var(--ink)">Orban Quill is exactly what our business has been lacking.</div>
    <div class="abs" style="left:81px;top:78px;font-size:10.5px;color:var(--muted)">Marta K.</div>
  </div>
</section>

<!-- About -->
<section>
  <div class="abs" style="left:0;top:674px;width:1200px;height:435px;background:var(--wash)"></div>
  <div class="label abs" style="left:87px;top:803px">ABOUT US</div>
  <h2 class="h2 abs" style="left:87px;top:831px;width:470px">Welcome to the Orban Quill Pharmacovigilance website.</h2>
  <p class="para abs" style="left:87px;top:932px;width:420px">We are an outsourcing partner to large and small companies within the pharmaceutical industry.</p>

  <div class="abs" style="left:625px;top:732px;width:528px;height:426px;background:var(--white);box-shadow:0 8px 30px rgba(30,40,80,.06)">
    <div class="abs" style="left:65px;top:88px;display:flex;align-items:baseline;gap:14px">
      <span style="font-family:'Yellowtail',cursive;font-size:54px;color:var(--red)">Our</span>
      <span style="font-size:56px;color:transparent;-webkit-text-stroke:1.2px var(--red);letter-spacing:1px">PRODUCTS</span>
    </div>
    <p class="para abs" style="left:65px;top:169px;width:390px">Our range of services is tailored to suit each of our client’s needs and cover both human and veterinary medicinal products.</p>
    <div class="abs" style="left:65px;top:293px;width:188px;height:65px;border:1px solid #cfd2da;display:flex;align-items:center;gap:14px;padding-left:27px;font-size:13px;color:var(--ink)">
      <span class="round" style="position:static;width:31px;height:31px;background:var(--red);display:flex;align-items:center;justify-content:center"><svg width="12" height="12" viewBox="0 0 12 12"><circle cx="6" cy="6" r="4.5" fill="none" stroke="#fff" stroke-width="1.2"/></svg></span>Human medicinal</div>
    <div class="abs" style="left:269px;top:293px;width:204px;height:65px;border:1px solid #cfd2da;display:flex;align-items:center;gap:14px;padding-left:25px;font-size:13px;color:var(--ink)">
      <span class="round" style="position:static;width:31px;height:31px;background:var(--blue);display:flex;align-items:center;justify-content:center"><svg width="12" height="12" viewBox="0 0 12 12"><path d="M2 10C2 5 5 2 10 2M5 10c0-3 2-5 5-5" fill="none" stroke="#fff" stroke-width="1.2"/></svg></span>Veterinary medicinal</div>
  </div>
</section>

<!-- Services -->
<section>
  <div class="abs" style="left:0;top:1468px;width:1200px;height:623px;background:var(--wash)"></div>
  <div class="label abs" style="left:87px;top:1191px">OUR SERVICES</div>
  <h2 class="h2 abs" style="left:87px;top:1220px">Orban Quill Quality services</h2>
  <div class="arrow" style="left:1035px;top:1227px;width:33px;height:33px"><svg width="13" height="9" viewBox="0 0 13 9"><path d="M13 4.5H1M4.5 1 1 4.5 4.5 8" fill="none" stroke="#1d2a4d" stroke-width="1.2"/></svg></div>
  <div class="arrow" style="left:1079px;top:1227px;width:33px;height:33px"><svg width="13" height="9" viewBox="0 0 13 9"><path d="M0 4.5h12M8.5 1 12 4.5 8.5 8" fill="none" stroke="#1d2a4d" stroke-width="1.2"/></svg></div>

  <div class="card" style="left:88px;top:1332px;width:272px;height:200px">
    <div class="svc-icon" style="background:var(--green)"><svg width="14" height="14" viewBox="0 0 14 14"><path d="M3 13h8M5 11V3h3v8M6 1h2" fill="none" stroke="#fff" stroke-width="1.2"/></svg></div>
    <div class="svc-title" style="left:84px">Medical Information</div>
    <p class="svc-text">Professional enquiry handling to support the safe and effective use of your products.</p>
  </div>
  <div class="card" style="left:397px;top:1332px;width:272px;height:200px">
    <div class="svc-icon" style="background:var(--red)"><svg width="14" height="13" viewBox="0 0 14 13"><path d="M7 12 1.5 6.5A3 3 0 0 1 7 2.5a3 3 0 0 1 5.5 4Z" fill="none" stroke="#fff" stroke-width="1.2"/></svg></div>
    <div class="svc-title" style="left:88px">Pharmacovigilance</div>
    <p class="svc-text">Ease the regulatory burden and keep compliant with current pharmacovigilance legislation.</p>
  </div>
  <div class="card" style="left:712px;top:1332px;width:272px;height:200px">
    <div class="svc-icon" style="background:var(--blue)"><svg width="14" height="12" viewBox="0 0 14 12"><rect x="1" y="1" width="12" height="10" fill="none" stroke="#fff" stroke-width="1.2"/><path d="M4 8V6M7 8V4M10 8V5" stroke="#fff" stroke-width="1.2"/></svg></div>
    <div class="svc-title" style="left:84px">Literature Monitoring</div>
    <p class="svc-text">Product safety through the surveillance of published articles and case reports.</p>
  </div>
  <div class="card" style="left:1027px;top:1332px;width:272px;height:200px">
    <div class="svc-icon" style="background:var(--yellow)"><svg width="14" height="12" viewBox="0 0 14 12"><rect x="1" y="1" width="12" height="8" fill="none" stroke="#fff" stroke-width="1.2"/><path d="M5 11h4" stroke="#fff" stroke-width="1.2"/></svg></div>
    <div class="svc-title" style="left:84px;color:var(--muted)">Training</div>
    <p class="svc-text" style="width:260px;white-space:nowrap;color:var(--muted)">Confident staff to support<br>pharmacovigilance processes</p>
  </div>
</section>

<!-- Testimonial -->
<section>
  <div class="label abs" style="left:87px;top:1648px">TESTIMONIAL</div>
  <h2 class="h2 abs" style="left:87px;top:1677px;width:400px">Here's a testimonial from our favorite clients</h2>
  <div class="round" style="left:984px;top:1665px;width:84px;height:84px;background:var(--red);display:flex;align-items:center;justify-content:center;color:#fff;font-size:40px;font-weight:700;line-height:1;padding-top:16px">”</div>

  <div class="abs" style="left:140px;top:1841px;width:919px;height:356px;background:var(--white);box-shadow:0 8px 30px rgba(30,40,80,.05)">
    <p class="abs" style="left:132px;top:98px;width:700px;font-size:22.5px;line-height:36px;color:var(--ink)">"Orban Quill is the most valuable business resource we have ever purchased. Orban Quill was the best investment I ever made. Orban Quill's got you covered. We have no regrets!"</p>
    <div class="round" role="img" aria-label="Client portrait" style="left:137px;top:246px;width:46px;height:46px;background:linear-gradient(135deg,#9fb7a4,#4c6a86)"></div>
    <div class="abs" style="left:204px;top:248px;font-size:17px;color:var(--ink)">Delia Harwood</div>
    <div class="abs" style="left:204px;top:272px;font-size:12px;color:var(--muted)">Clinic team</div>
  </div>
  <div class="arrow" style="left:45px;top:1976px;width:32px;height:32px"><svg width="13" height="9" viewBox="0 0 13 9"><path d="M13 4.5H1M4.5 1 1 4.5 4.5 8" fill="none" stroke="#1d2a4d" stroke-width="1.2"/></svg></div>
  <div class="arrow" style="left:1119px;top:1976px;width:32px;height:32px"><svg width="13" height="9" viewBox="0 0 13 9"><path d="M0 4.5h12M8.5 1 12 4.5 8.5 8" fill="none" stroke="#1d2a4d" stroke-width="1.2"/></svg></div>
</section>

<!-- Call to action -->
<section class="abs" style="left:0;top:2259px;width:1200px;height:313px;background:var(--red)">
  <div class="round" style="left:74px;top:67px;width:44px;height:44px;border:1.5px solid #fff;display:flex;align-items:center;justify-content:center"><svg width="14" height="14" viewBox="0 0 14 14"><path d="M3 13h8M5 11V3h3v8M6 1h2" fill="none" stroke="#fff" stroke-width="1.2"/></svg></div>
  <div class="round" style="left:223px;top:156px;width:68px;height:68px;border:2px solid #fff;display:flex;align-items:center;justify-content:center"><svg width="28" height="26" viewBox="0 0 28 26"><rect x="2" y="6" width="24" height="18" rx="3" fill="none" stroke="#fff" stroke-width="2"/><path d="M10 6V2h8v4M14 11v8M10 15h8" fill="none" stroke="#fff" stroke-width="2"/></svg></div>
  <div class="round" style="left:1008px;top:75px;width:113px;height:113px;border:2.5px solid #fff;display:flex;align-items:center;justify-content:center"><svg width="40" height="36" viewBox="0 0 40 36"><path d="M20 33 5 18A9 9 0 0 1 20 6a9 9 0 0 1 15 12Z" fill="none" stroke="#fff" stroke-width="2.5"/><path d="M6 18h9l3-5 4 9 3-4h9" fill="none" stroke="#fff" stroke-width="2"/></svg></div>
  <div class="abs" style="left:0;top:80px;width:1200px;text-align:center;font-size:13.5px;color:#fff">READY TO GET STARTED ?</div>
  <div class="abs" style="left:0;top:107px;width:1196px;text-align:center;font-size:31px;color:#fff">Get in touch with us</div>
  <a class="btn" style="left:511px;top:169px;width:177px;height:61px;background:#fff;color:var(--red)">Contact us</a>
</section>

<!-- Footer -->
<footer class="abs" style="left:0;top:2572px;width:1200px;height:412px;background:var(--wash)">
  <div class="brand abs" style="left:87px;top:84px"><i></i>OrbanQuill.</div>
  <div class="abs" style="left:358px;top:85px"><div class="foot-h">Navigation</div><div class="foot-l" style="margin-top:10px">Home<br>About us<br>Client<br>Contact</div></div>
  <div class="abs" style="left:483px;top:85px"><div class="foot-h">Product</div><div class="foot-l" style="margin-top:10px">Services<br>Testimonial<br>Qppv<br>Privacy Policy</div></div>
  <div class="abs" style="left:608px;top:85px"><div class="foot-h">Adress</div><div class="foot-l" style="margin-top:10px">14 Alder Row, England UK.<br>hello@orbanquill.co.uk</div></div>
  <div class="abs" style="left:608px;top:189px;width:191px;height:37px;background:#fff;border-radius:4px;box-shadow:0 3px 10px rgba(30,40,80,.08);display:flex;align-items:center;padding-left:14px;gap:8px">
    <span class="round" style="position:static;width:14px;height:14px;background:#22c3c3;display:flex;align-items:center;justify-content:center"><svg width="8" height="8" viewBox="0 0 8 8"><path d="M1.5 1c0 3 2.5 5.5 5.5 5.5L7 5 5.5 4.5 4.8 5.2A4 4 0 0 1 2.8 3.2l.7-.7L3 1Z" fill="#fff"/></svg></span>
    <span style="font-size:6px;color:var(--muted)">Call us on</span>
    <span style="font-size:10.5px;letter-spacing:2px;color:var(--ink);font-weight:500">0300-5550-182</span>
  </div>
  <div class="abs foot-h" style="left:879px;top:85px">Social Media</div>
  <div class="round" role="img" aria-label="Social network link" style="left:879px;top:130px;width:46px;height:46px;background:var(--ink)"></div>
  <div class="round" role="img" aria-label="Social network link" style="left:939px;top:130px;width:46px;height:46px;background:var(--red);box-shadow:0 6px 14px rgba(236,58,59,.3)"></div>
  <div class="round" role="img" aria-label="Social network link" style="left:996px;top:130px;width:46px;height:46px;background:var(--ink)"></div>
  <div class="abs" style="left:0;top:350px;width:1200px;text-align:center;font-size:11px;color:var(--ink)">© Orban Quill Company - All Rights Reserved</div>
  <div class="abs" style="left:0;top:370px;width:1200px;text-align:center;font-size:7.5px;color:var(--ink)">Terms &amp; Conditions | Privacy Policy | Contact Us</div>
</footer>

</body>
</html>
```